International trading company needs banner designs for university careers fairs. Additional work to

Description
Our company, Meridale Capital, operates in the finance industry. We trade numerous financial instruments across the globe. We focus on futures, options, etfs and are currently expanding into the exciting area of cryptocurrencies. A main focus of ours is to use a systematic and quantitative approach to trading to develop and refine trading strategies that are relatively low risk in nature, but are scalable and provide positive returns. We work hard, we push each other to achieve great results. But at the same time we really enjoy each other’s company and share a relaxed atmosphere at work. Our website is http://www.meridalecapital.com.au/. Meridale will be attending university careers fairs and expos in coming months to attract the very best talent there is for graduate trading roles as well as graduate developer roles. As such, we require our booth to look professional. We want to convey our message that a career with us is exciting, rewarding, but also challenging. We aim to nurture talent and hope to provide the tools necessary to strive in a career in trading.

We have 3 aspects to our booth concept. But for this designer contest, we will focus on 1 of those projects. When we decide on one designer, we hope they will be willing to work one on one on the other 2 projects. On top of this contest, we are willing to pay $250 for the additional 2 projects, one of which is quite simple in design brief, the other will allow the designer the flare to be creative. It is important to note that all three concepts need to be cohesive. Each concept should complement the other in colour as well as message.

For the entire project to be finished, we are a little rushed on time and would require completion of all three concepts by February 2nd.

We will only require soft copy files so we can manage the print ourselves. We can accept a vector, eps or ai file.

For this contest project, the design concept is a pull-up banner. We will have 3 pull-up banners each with slightly different messages.

We have attached pictures to help inspire the designer. Also, we have attached company logo (a unicorn) and name, along with varying colour vectors.

Meridale Capital’s primary colours are black, green and white. We would like all 3 banners to be in the same scheme. But we are happy to see slightly different variations in design options on the colour scheme. We do feel that green writing on black background would look the sharpest and have the most impact. We could be wrong though and are fine to see different designs.

The banner dimensions will be 85cm wide x 210cm tall. So there is room on the banner to deliver an exciting, yet professional message.

Preliminary Pull-up Banner ideas
We are not designers, we are open to you, the designer, using your creative flare to design 3 sharp looking banners. We do have a rough idea of the direction of each banner though.

Banner 1 – A company inspired banner. We would like our company name, our logo (prominent!) and beneath it 3 to 4 words that describe what we’re about. For example, Challenging, Rewarding, Passionate, Entrepreneurial, Focused, Collaborative, Innovative, Systematic, Strategic. Happy for the designer to take control here.

For the rest of the banner we are open to design. Potentially a picture taken from our website that is reflective of our culture – which is relaxed, hard-working, collaborative, rewarding.

It doesn’t need to be too busy or cluttered, so no need to throw in designs that aren’t really consistent with us.

Banner 2 – A trader inspired banner. This is more designed to attract graduates interested in a career in trading. Include meridale name and logo. Maybe include a question for the students... Something like,
“Want to be challenged?
Want to strategise?
Want to be rewarded?
Become a trader!”
Doesn’t have to be straight angles, can be on an angle – designer free reign here. Also we can have different sentences, words. Up to the designer. We would like to include something that would attract a trader’s mind, something visual, like a trading chart. See attached pictures for trading chart examples.

Somewhere on the banner we can mention Graduate Trader Program, please contact us at careers@meridalecapital.com.au. Phone number below it (02) 7156 4830.

Banner 3 - A developer inspired banner. This is more designed to attract graduates interested in a career in developing. Include meridale name and logo

Put the following pitch on the banner and fill the rest of the space with designs and pictures. No fixed layout required here.

Good at problem solving? Obsessed with creating quality software? Love working with numbers? Do you speak programming language? Want to face fresh challenges each day?

On the banner we can mention Graduate Software Engineer Program, please contact us at careers@meridalecapital.com.au. Phone number below it (02) 7156 4830.

Additionally to the above 3 banners, we had an idea of including random words across the banners in random sizes and boldness. We’re not sure how this would appear so we would like to see a couple designs on this. We thought we could have a top tier of buzz words that should be more prominent with the second tier buzzwords in smaller size. Two design types - randomly displayed, secondly a bit more structured. Can decide what looks best when we receive design. Words below. We don’t have to include all of these words, whatever a good design lends itself to. Words should only be in green, black or white - consistent with our company scheme.

Top Tier Buzzwords
Trading
Cryptocurrency
Options
Market making
Trading
Bitcoin
Derivatives
ETF
Futures
Volatility
Arbitrage
Technology
HFT
Hedging

Second Tier Buzzwords
R&K 400
QMB 300
VLZ
DWT
QMB
FX
Bid
Offer
Margining
Long
Short
Spot
Position
Tolvar
Brimo
Wel Daro
WDI
GGI
Buy
Sell
Delta
Gamma
Vega
Theta
Skew
Straddle
Call

Once we have selected the designer, we are keen that they would complete another 2 projects for us. The other 2 projects are as follows:
• A double sided A5 flyer design – This should provide more information about what Meridale can offer the students as a career and a workplace. We will also give a small amount of detail about the graduate program.
• Table Cloth design – At each exhibition we receive a table at our booth. We would like to have a logo laden table cloth that will look professional

We would like the design scheme to flow neatly from the banners to the flyers to the table cloth. So the colours are consistent and our general tone/message is also consistent.

We have attached pictures that should help the designer. Included pictures of pull-up banners, pictures of student careers fairs, flyers, table cloth dimensions, Meridale’s logos and colour vectors.

Preliminary Double sided A5 Flyer ideas.

We would need two designs – a trader design and a developer design.

Art file to be supplied PDF file with trim marks & 3mm bleed

With the flyer we would like to add a little more information about Meridale on the front page (which should be the same for the trader flyer and the developer flyer). On the back page we would be a little more detailed in the graduate program. Give dates, the onboarding process, rough program details/info.

Front Page – Include Meridale name, logo. Explanation of who we are - proprietary trading firm, using our own capital to trade financial instruments around the world. We trade futures, options, etfs and cryptocurrencies (can make more elaborate).

To make it sound interesting we’d like to explain potential for growth in certain markets. So something along the lines, of “We are seeing rapid expansion in certain markets. At meridale we are always looking for new strategies and talent to expand our already growing presence. Working with Meridale, you’ll get exposure and experience on all of these exciting markets which will greatly benefit you in your career progression” (Doesn’t need to be word for word)

We’d also like to mention some of the perks of working with us:
daily lunch provided
cafe coffee
 breakfast/snacks
 casual attire
 cash bonus half yearly
 competitive rates
 team dinners
 gym membership
 company trips
We’d like to use consistent colour schemes with our company, Black and Green. Some white could work in there. But not a necessity.
The designer can feel free to add in some sharp looking images.

Back Page Trader Flyer - We would like to give some more info on the positives of the trader program. We’re mainly focusing on the strengths of the program here – listed below.
• 1 on 1 training
• In-depth theory classes with practical applications
• Experienced traders providing the training
• Live trading within 3 months
• Ongoing mentoring
• Exposure to different markets/strategies
• Placed onto products that best suit their strengths
• Simulated trader training based on actual events

We should also add contact details for students to apply to.
For more information on the Graduate Trader Program
contact us at careers@meridalecapital.com.au.
Phone number (02) 7156 4830.

OR

To apply please send through your CV and academic transcript to careers@meridalecapital.com.au

We would also want this to look quite sharp, so adding in a trading graph could make it look exciting and attractive.

Back Page Developer Flyer
• 1 on 1 mentoring by senior software engineers
• Full SDLC exposure
• Extremely agile environment
• Direct interaction with business and stakeholders
• Multiple career paths for future growth

For more information on the Graduate Software Engineer Program
Contact us at careers@meridalecapital.com.au.

OR

Preliminary table cloth ideas.
We would need two designs before choosing one.

First design is a very simple design that would look professional. A plain black design with MERIDALE on the front in Green.

The second design is plain black, MERIDALE on the front in Green, similar to above. But we’d also like to see the words mentioned above in the top tier and second tier randomly across the table cloth. In different sizes and weightings.
We’ll see which design looks the best and choose one.

References to see the products we’d be using:
https://brontelsigns.com.au/products/pull-up-banners
https://www.quorvelprint.com.au/lpt/flyers-sizes.aspx?mk=flyers+design&rd=1
https://www.tallowbanners.com.au/outdoor/custom-table-throws/loose-printed-table-throws.html

Target Market(s)

University Graduates in IT, Engineering, Maths, Sciences, Business that would be interested in a career of trading financial instruments including cryptocurrency, options, futures, ETFs. We are also targeting developers in the same space.

Industry/Entity Type

Finance

Font styles to use
Serif
Sans Serif

Colors
00a990
ffffff
000000
33b8a4
1b1b1b

Requirements
Must have
• Cohesion between banners and other project work.
• Clear message coming through
• Professional look
• Eye catching
• Attractive
• Colour schemes must work
Should not have
• Must not be boring. We are looking to project our company image. We are not boring so we want to see some creative flare. But we are also a professional firm so our designs must be sharp.

```html
<!DOCTYPE html>
<html lang="en">
<head>
<meta charset="utf-8">
<title>Meridale Capital – Pull-up Banner</title>
<link rel="stylesheet" href="https://fonts.googleapis.com/css2?family=Josefin+Sans:wght@300&family=Oswald:wght@500&family=Roboto:wght@400;700&display=swap">
<style>
  :root {
    --green: #33b8a4;
    --green-deep: #00a990;
    --black: #000000;
    --ink: #1b1b1b;
    --white: #ffffff;
    --stage: #2a2a2a;
  }
  html, body {
    margin: 0;
    padding: 0;
    width: 1200px;
    height: 1000px;
    overflow: hidden;
    background: var(--stage);
  }
  .banner {
    position: absolute;
    left: 418px;
    top: 50px;
    width: 364px;
    height: 900px;
    background: var(--white);
    overflow: hidden;
    box-shadow: 0 10px 40px rgba(0,0,0,.5);
  }
  .brand-name {
    position: absolute;
    top: 52px;
    left: 0;
    width: 100%;
    text-align: center;
    font-family: "Josefin Sans", sans-serif;
    font-weight: 300;
    font-size: 46px;
    letter-spacing: 2px;
    color: var(--green);
    margin: 0;
  }
  .team-photo {
    position: absolute;
    top: 140px;
    left: 0;
    width: 100%;
    height: 360px;
    background: linear-gradient(180deg, #ffffff 0%, #eef0f1 22%, #d6d8db 48%, #8f93a3 72%, #2f3358 100%);
  }
  .lower-panel {
    position: absolute;
    left: 0;
    top: 0;
    width: 364px;
    height: 900px;
  }
  .values {
    list-style: none;
    margin: 0;
    padding: 0;
  }
  .value {
    position: absolute;
    display: flex;
    align-items: center;
    gap: 18px;
  }
  .value-icon {
    width: 60px;
    height: 60px;
    flex: none;
  }
  .value-label {
    font-family: "Oswald", sans-serif;
    font-weight: 500;
    font-size: 25px;
    color: var(--green);
    letter-spacing: .3px;
  }
  .value--challenging { left: 31px; top: 507px; }
  .value--rewarding   { left: 120px; top: 585px; }
  .value--focused     { left: 62px; top: 669px; }
  .value--innovative  { left: 152px; top: 746px; }
  .website {
    position: absolute;
    top: 840px;
    left: 0;
    width: 100%;
    text-align: center;
    font-family: "Roboto", sans-serif;
    font-size: 16px;
    color: var(--green);
    margin: 0;
  }
  .website strong { font-weight: 700; }
</style>
</head>
<body>
  <main class="banner">
    <h1 class="brand-name">MERIDALE</h1>

    <div class="team-photo" role="img" aria-label="Photo of two colleagues working together at trading desks with monitors in a bright office"></div>

    <svg class="lower-panel" viewBox="0 0 364 900" aria-hidden="true">
      <path d="M0,366 C80,428 160,478 240,474 C300,471 340,462 364,454 L364,900 L0,900 Z" fill="var(--green)"/>
      <path d="M0,382 C80,444 160,492 240,490 C300,488 340,480 364,472 L364,900 L0,900 Z" fill="var(--black)"/>
    </svg>

    <ul class="values">
      <li class="value value--challenging">
        <svg class="value-icon" viewBox="0 0 60 60" aria-hidden="true">
          <circle cx="30" cy="30" r="28" fill="none" stroke="var(--green)" stroke-width="2"/>
          <circle cx="30" cy="30" r="23" fill="none" stroke="var(--green)" stroke-width="1"/>
          <path d="M18,32 C16,24 22,18 30,19 C38,18 44,23 42,31 C43,36 38,40 33,39 L32,43 L27,43 L27,39 C21,40 17,37 18,32 Z" fill="var(--green)"/>
        </svg>
        <span class="value-label">CHALLENGING</span>
      </li>
      <li class="value value--rewarding">
        <svg class="value-icon" viewBox="0 0 60 60" aria-hidden="true">
          <circle cx="30" cy="30" r="28" fill="none" stroke="var(--green)" stroke-width="2"/>
          <circle cx="30" cy="30" r="23" fill="none" stroke="var(--green)" stroke-width="1"/>
          <rect x="18" y="25" width="24" height="6" fill="var(--green)"/>
          <rect x="20" y="32" width="20" height="12" fill="var(--green)"/>
          <rect x="28.5" y="25" width="3" height="19" fill="var(--black)"/>
          <path d="M30,25 C26,17 20,20 24,24 Z M30,25 C34,17 40,20 36,24 Z" fill="var(--green)"/>
        </svg>
        <span class="value-label">REWARDING</span>
      </li>
      <li class="value value--focused">
        <svg class="value-icon" viewBox="0 0 60 60" aria-hidden="true">
          <circle cx="30" cy="30" r="28" fill="none" stroke="var(--green)" stroke-width="2"/>
          <circle cx="30" cy="30" r="23" fill="none" stroke="var(--green)" stroke-width="1"/>
          <circle cx="29" cy="31" r="13" fill="none" stroke="var(--green)" stroke-width="2.5"/>
          <circle cx="29" cy="31" r="7.5" fill="none" stroke="var(--green)" stroke-width="2.5"/>
          <circle cx="29" cy="31" r="2.5" fill="var(--green)"/>
          <path d="M29,31 L42,18 M38,17 L43,17 L43,22" fill="none" stroke="var(--green)" stroke-width="2.5"/>
        </svg>
        <span class="value-label">FOCUSED</span>
      </li>
      <li class="value value--innovative">
        <svg class="value-icon" viewBox="0 0 60 60" aria-hidden="true">
          <circle cx="30" cy="30" r="28" fill="none" stroke="var(--green)" stroke-width="2"/>
          <circle cx="30" cy="30" r="23" fill="none" stroke="var(--green)" stroke-width="1"/>
          <path d="M25,38 C25,33 21,31 21,26 C21,21 25,18 30,18 C35,18 39,21 39,26 C39,31 35,33 35,38 Z" fill="none" stroke="var(--green)" stroke-width="2"/>
          <path d="M26,41 L34,41 M27,44 L33,44" stroke="var(--green)" stroke-width="2"/>
          <path d="M30,10 L30,14 M17,15 L19.5,17.5 M43,15 L40.5,17.5 M13,26 L16,26 M44,26 L47,26" stroke="var(--green)" stroke-width="1.5"/>
        </svg>
        <span class="value-label">INNOVATIVE</span>
      </li>
    </ul>

    <p class="website">www.<strong>meridalecapital</strong>.com.au</p>
  </main>
</body>
</html>
```